Private chef located in Vail, CO

I would like my info located at the top of the landing page, perhaps some Vail mountain landscapes that I could swap out from summer to winter photos. I need the menu bar to have a link to a blog, about me, photo gallery, recipes & beer reviews. I would also like to have a shop, but only populated with products from zellora or other online retailers that I can affiliate with.
Target Market(s)
Extremely wealthy, affluent people, concierge, international
Number of Pages Required
5+ page

```html
<!DOCTYPE html>
<html lang="en">
<head>
<meta charset="utf-8">
<title>Daniel Whitcombe – Private Chef in Vail</title>
<link rel="stylesheet" href="https://fonts.googleapis.com/css2?family=Montserrat:wght@400;600;700&family=Poppins:wght@300;400;500;600&family=Oswald:wght@400;500&family=Roboto:wght@400;700&display=swap">
<style>
:root{
  --orange:#f0672a;
  --blue:#1a5fc4;
  --ink:#1c1c1c;
  --muted:#555;
  --sky-top:#2f77c9;
  --sky-mid:#8fc1ee;
  --sky-low:#eef6fd;
  --dark:#151515;
  --footer:#f3f3f3;
}
*{box-sizing:border-box;margin:0;padding:0}
html,body{width:1200px;height:4369px;overflow:hidden}
body{position:relative;font-family:"Poppins",sans-serif;color:var(--ink);background:#fff}
.abs{position:absolute}
.center{text-align:center}

.site-header{position:absolute;left:0;top:0;width:1200px;height:95px;background:#fff;display:flex;align-items:center;justify-content:space-between;padding:0 100px}
.brand{font-family:"Poppins",sans-serif;font-weight:500;font-size:36px;color:var(--ink)}
.nav{display:flex;gap:20px;font-family:"Oswald",sans-serif;font-size:17px;text-transform:uppercase}
.nav a{color:var(--ink);text-decoration:none}
.nav a.active{color:var(--orange)}

.hero{position:absolute;left:0;top:95px;width:1200px;height:630px;background:linear-gradient(180deg,#35577c 0%,#8ea9c3 30%,#d9e2ea 48%,#9aa6ad 62%,#4a5247 80%,#2e3329 100%)}
.hero-title{position:absolute;top:205px;width:100%;text-align:center;color:#fff;font-family:"Roboto",sans-serif;font-size:50px;font-weight:400;letter-spacing:1px}
.hero-title b{font-weight:700}
.hero-sub{position:absolute;top:280px;width:100%;text-align:center;color:#fff;font-family:"Roboto",sans-serif;font-weight:700;font-size:32px}
.btn{display:inline-block;background:var(--orange);color:#fff;font-family:"Poppins",sans-serif;font-weight:600;text-transform:uppercase;text-align:center;border-radius:26px}
.hero .btn{position:absolute;left:510px;top:353px;width:180px;height:44px;line-height:44px;font-size:16px}
.dots{position:absolute;top:443px;left:0;width:100%;display:flex;justify-content:center;gap:8px}
.dots span{width:14px;height:14px;border-radius:50%;border:2px solid #fff}
.dots span.on{background:#fff}

.about-frame{position:absolute;border:3px solid var(--blue)}
.about-photo{position:absolute;left:145px;top:860px;width:415px;height:350px;background:linear-gradient(150deg,#5b5650,#2a2826 55%,#8a6b43)}
.about-heading{position:absolute;left:642px;top:830px;font-family:"Montserrat",sans-serif}
.about-heading h2{font-size:38px;font-weight:700;line-height:1.1}
.about-heading p{font-size:38px;font-weight:400}
.about-text{position:absolute;left:642px;top:965px;width:440px;font-size:14px;line-height:33px;color:var(--muted)}
.btn-sq{position:absolute;left:642px;top:1195px;width:152px;height:40px;line-height:40px;font-size:13px;border-radius:3px;background:var(--orange);color:#fff;font-weight:600;text-align:center;box-shadow:0 3px 6px rgba(0,0,0,.2)}

.sky{position:absolute;left:0;top:1368px;width:1200px;height:1505px;background:linear-gradient(180deg,var(--sky-top) 0%,#5b9fe0 15%,var(--sky-mid) 30%,#dcecf9 42%,var(--sky-low) 52%,#fff 100%)}
.sec-title{position:absolute;width:100%;text-align:center;font-family:"Montserrat",sans-serif;font-size:40px}
.rule{position:absolute;left:558px;width:84px;height:3px}
.service{position:absolute;top:1670px;width:220px;height:305px;background:#fff;text-align:center;padding:0 18px;box-shadow:0 2px 8px rgba(0,0,0,.1)}
.service.feature{top:1650px;height:343px;background:var(--blue);color:#fff}
.service h3{font-family:"Montserrat",sans-serif;font-size:16px;font-weight:700;margin-top:14px;text-transform:uppercase}
.service p{font-size:12.5px;line-height:22px;margin-top:10px;color:var(--muted)}
.service.feature p{color:#e8efff}
.icon{margin-top:38px}

.gift{position:absolute;top:2325px;width:279px;height:420px}
.gift-img{height:235px}
.gift-card{position:absolute;left:18px;top:165px;width:243px;height:210px;background:#fff;text-align:center;box-shadow:0 1px 5px rgba(0,0,0,.12)}
.price{font-family:"Montserrat",sans-serif;font-weight:700;font-size:24px;color:var(--orange);margin-top:12px}
.people{font-size:13px;color:var(--orange)}
.gift-card p{font-size:12.5px;line-height:22px;color:var(--muted);padding:12px 16px 0}
.gift .btn-book{position:absolute;left:18px;top:375px;width:243px;height:45px;line-height:45px;background:var(--orange);color:#fff;text-align:center;font-family:"Montserrat",sans-serif;font-weight:700;font-size:17px}

.recipes{position:absolute;left:0;top:2873px;width:1200px;height:524px;background:radial-gradient(ellipse at 70% 85%,#3a3027,var(--dark) 60%)}
.quote{position:absolute;top:210px;width:290px;color:#fff}
.avatar{position:absolute;left:0;top:0;width:70px;height:70px;border-radius:50%;background:#d8d2cc;border:3px solid #fff}
.quote p{margin-left:95px;font-size:12.5px;line-height:22px}
.quote .name{margin-left:95px;font-size:12.5px;font-style:italic;margin-top:10px}
.stars{margin-left:95px;color:var(--orange);font-size:17px;letter-spacing:2px}
.arrow-btn{position:absolute;top:432px;width:26px;height:26px;border:2px solid #fff;border-radius:50%;color:#fff;text-align:center;line-height:20px;font-size:14px}

.book-text{position:absolute;top:3590px;width:100%;text-align:center;font-size:17px;line-height:42px;color:#333}
.btn-outline{position:absolute;left:508px;top:3705px;width:184px;height:52px;line-height:48px;border:2px solid var(--orange);color:var(--orange);text-align:center;font-weight:600;font-size:16px;text-transform:uppercase}

.footer{position:absolute;left:0;top:3862px;width:1200px;height:383px;background:var(--footer)}
.fcol{position:absolute;top:95px}
.fcol h4{font-family:"Montserrat",sans-serif;font-size:17px;font-weight:700;text-transform:uppercase;margin-bottom:26px}
.fcol p,.fcol li{font-size:13px;line-height:20px;color:#333}
.fcol ul{list-style:none}
.fcol li{line-height:26px}
.cards{display:flex;gap:6px}
.cards span{width:40px;height:26px;border-radius:3px;background:#c9ced6}
.socials{display:flex;gap:6px;margin-top:20px}
.socials span{width:26px;height:26px;border-radius:50%;border:1px solid #555}
.input{width:270px;height:34px;border-radius:17px;background:#fff;border:1px solid #ddd;font-size:11px;color:#999;padding:9px 16px;margin-top:18px}
.btn-sub{width:135px;height:34px;line-height:34px;font-size:13px;margin-top:16px;border-radius:17px}
.contact-row{display:flex;gap:18px;margin-bottom:18px}
.bottom-bar{position:absolute;left:0;top:4245px;width:1200px;height:124px;background:#fff;text-align:center;line-height:124px;font-size:13px;color:#333}
</style>
</head>
<body>

<header class="site-header">
  <div class="brand">Daniel Whitcombe</div>
  <nav class="nav">
    <a class="active" href="#">Home</a><a href="#">Blog</a><a href="#">About Me</a><a href="#">Photo Gallery</a><a href="#">Recipes &amp; Beer Reviews</a><a href="#">Contact Us</a>
  </nav>
</header>

<section class="hero" role="img" aria-label="Snowy Vail mountain landscape with pine forest">
  <h1 class="hero-title">CHEF <b>DANIEL WHITCOMBE</b></h1>
  <div class="hero-sub">Private Chef In Vail</div>
  <span class="btn">Book Now!</span>
  <div class="dots"><span class="on"></span><span></span><span></span></div>
</section>

<div class="about-frame" style="left:120px;top:837px;width:420px;height:350px"></div>
<div class="about-frame" style="left:170px;top:882px;width:420px;height:350px"></div>
<div class="about-photo" role="img" aria-label="Chef in a cap smiling beside a roasted turkey in the oven"></div>
<div class="about-heading"><h2>About</h2><p>Daniel Whitcombe</p></div>
<p class="about-text">I have been cooking my whole life, I spent my late 20's cooking for professional athletes, this led me to pursue cooking professionally. I have cooked through Central America, living in Costa Rica and Panama. I have been based in Vail the past few years, taking a year hiatus to Chicago to work in some award-winning restaurants &amp; gain experience working</p>
<div class="btn-sq">Learn More &#10140;</div>

<section class="sky" role="img" aria-label="Blue sky fading over snowy mountain peaks"></section>
<h2 class="sec-title" style="top:1445px;color:#fff"><b>OUR</b> SERVICES</h2>
<div class="rule" style="top:1520px;background:#fff"></div>
<p class="abs center" style="top:1553px;width:100%;color:#fff;font-size:18px">As a professional Chef, I offer the following services</p>

<div class="service" style="left:137px">
  <svg class="icon" width="92" height="92" viewBox="0 0 92 92"><circle cx="46" cy="46" r="42" fill="none" stroke="#1a5fc4" stroke-width="3"/><path d="M28 58h36M32 58v-8h28v8M40 50v-12h12v12M46 30v8" fill="none" stroke="#1a5fc4" stroke-width="3"/></svg>
  <h3>Catering</h3>
  <p>I can provide catering services in Vail for weddings, birthdays, corporate events and more.</p>
</div>
<div class="service feature" style="left:372px">
  <svg class="icon" width="100" height="100" viewBox="0 0 100 100" style="margin-top:30px"><circle cx="50" cy="50" r="48" fill="#fff"/><circle cx="50" cy="40" r="12" fill="none" stroke="#1a5fc4" stroke-width="3"/><path d="M30 78c0-14 9-22 20-22s20 8 20 22M38 26h24" fill="none" stroke="#1a5fc4" stroke-width="3"/></svg>
  <h3>Personal<br>Chef</h3>
  <p>I can create a menu based on your preferences to enjoy in the comfort of your home in Vail. Simply tell me what</p>
</div>
<div class="service" style="left:608px">
  <svg class="icon" width="92" height="92" viewBox="0 0 92 92"><circle cx="46" cy="46" r="42" fill="none" stroke="#1a5fc4" stroke-width="3"/><circle cx="46" cy="40" r="12" fill="none" stroke="#1a5fc4" stroke-width="3"/><path d="M28 70c0-10 8-16 18-16s18 6 18 16" fill="none" stroke="#1a5fc4" stroke-width="3"/></svg>
  <h3>Full-Time Chef</h3>
  <p>Enjoy the services of a private chef during your holidays in Vail.</p>
</div>
<div class="service" style="left:841px">
  <svg class="icon" width="92" height="92" viewBox="0 0 92 92"><circle cx="46" cy="46" r="42" fill="none" stroke="#1a5fc4" stroke-width="3"/><circle cx="46" cy="48" r="16" fill="none" stroke="#1a5fc4" stroke-width="3"/><path d="M24 30v36M68 30v36" stroke="#1a5fc4" stroke-width="3"/></svg>
  <h3>Prepped Meals</h3>
  <p>Weekly healthy meals in Vail, prepared in your home or delivered once per week.</p>
</div>

<h2 class="sec-title" style="top:2093px;font-weight:600;letter-spacing:1px">GIFT A PRIVATE CHEF EXPERIENCE</h2>
<div class="rule" style="top:2170px;background:var(--orange)"></div>
<p class="abs center" style="top:2200px;width:100%;font-size:18px;line-height:38px;color:#333">Surprise your family with a private chef for a unique dining experience<br>anywhere in the United States</p>

<div class="gift" style="left:143px">
  <div class="gift-img" role="img" aria-label="Plated dish with fresh vegetables" style="background:linear-gradient(135deg,#3c2a1c,#b07a3c,#2b1d14)"></div>
  <div class="gift-card"><div class="price">$240.00</div><div class="people">2 people</div><p>Gift a dinner for two with a personal chef at home. Enjoy creative cuisine and a unique experience.</p></div>
  <div class="btn-book">BOOK NOW</div>
</div>
<div class="gift" style="left:460px">
  <div class="gift-img" role="img" aria-label="Plated dish with red garnish and greens" style="background:linear-gradient(135deg,#2a1a14,#7a2a20,#3a4a22)"></div>
  <div class="gift-card"><div class="price">$300.00</div><div class="people">2 people</div><p>Gift a gourmet dinner for two with a personal chef at home. Savour dishes from our best chefs, creators of signature</p></div>
  <div class="btn-book">BOOK NOW</div>
</div>
<div class="gift" style="left:777px">
  <div class="gift-img" role="img" aria-label="Gourmet plated main course" style="background:linear-gradient(135deg,#4a3a2a,#8a6a40,#2e2418)"></div>
  <div class="gift-card"><div class="price">$400.00</div><div class="people">2 people</div><p>Gift a truly gastronomic experience, with a menu for two from a critically acclaimed personal chef with experience in</p></div>
  <div class="btn-book">BOOK NOW</div>
</div>

<section class="recipes" role="img" aria-label="Dark kitchen scene with chef plating food">
  <h2 class="sec-title" style="top:77px;color:#fff;font-weight:700">RECIPES &amp; BEER REVIEWS</h2>
  <div class="rule" style="top:150px;background:var(--orange)"></div>
  <div class="quote" style="left:140px"><div class="avatar"></div><p>&ldquo; At vero eos et accusamus et iusto odio dignissimos ducimus qui blanditiis praesentium voluptatum deleniti atque corrupti</p><div class="name">Marcus Hale</div><div class="stars">&#9733;&#9733;&#9733;&#9733;&#9734;</div></div>
  <div class="quote" style="left:450px"><div class="avatar"></div><p>&ldquo; At vero eos et accusamus et iusto odio dignissimos ducimus qui blanditiis praesentium voluptatum deleniti atque corrupti</p><div class="name">Marcus Hale</div><div class="stars">&#9733;&#9733;&#9733;&#9733;&#9734;</div></div>
  <div class="quote" style="left:760px"><div class="avatar"></div><p>&ldquo; At vero eos et accusamus et iusto odio dignissimos ducimus qui blanditiis praesentium voluptatum deleniti atque corrupti</p><div class="name">Marcus Hale</div><div class="stars">&#9733;&#9733;&#9733;&#9733;&#9734;</div></div>
  <div class="arrow-btn" style="left:565px">&lsaquo;</div>
  <div class="arrow-btn" style="left:597px">&rsaquo;</div>
</section>

<h2 class="sec-title" style="top:3488px;font-weight:600;letter-spacing:1px">BOOK YOUR EXPERIENCE WITH DANIEL</h2>
<div class="rule" style="top:3565px;background:var(--orange)"></div>
<p class="book-text">Specify the details of your requests and our Chefs will send<br>you a customised menu.</p>
<div class="btn-outline">Book Now!</div>

<footer class="footer">
  <div class="fcol" style="left:126px">
    <h4>Secure Payment</h4>
    <div class="cards"><span></span><span></span><span></span><span></span></div>
    <div class="socials"><span></span><span></span><span></span><span></span></div>
  </div>
  <div class="fcol" style="left:362px;width:290px">
    <h4>Sign Up For Newsletter</h4>
    <p>Excepteur sint occaecat cupidatat non proident, sunt in culpa qui officia deserunt</p>
    <div class="input">Enter email</div>
    <div class="btn btn-sub">Subscribe</div>
  </div>
  <div class="fcol" style="left:682px;width:260px">
    <h4>Contact Us</h4>
    <div class="contact-row"><svg width="16" height="20" viewBox="0 0 16 20"><path d="M8 0a7 7 0 0 0-7 7c0 5 7 13 7 13s7-8 7-13a7 7 0 0 0-7-7zm0 10a3 3 0 1 1 0-6 3 3 0 0 1 0 6z" fill="#333"/></svg><p>Daniel Whitcombe<br>12 Aspen Ridge Lane<br>Vail CO 81657</p></div>
    <div class="contact-row"><svg width="16" height="16" viewBox="0 0 16 16"><path d="M3 1l3 3-2 2c1 2 3 4 5 5l2-2 3 3-2 3C6 15 1 10 0 3z" fill="#333"/></svg><p>Phone:<br>+1 970 555 0148</p></div>
    <div class="contact-row"><svg width="16" height="14" viewBox="0 0 16 14"><path d="M0 1h16v12H0zM0 1l8 6 8-6" fill="none" stroke="#333" stroke-width="2"/></svg><p>Email:<br>info@danielwhitcombe.com</p></div>
  </div>
  <div class="fcol" style="left:952px">
    <h4>Quick Links</h4>
    <ul><li>Select a Country</li><li>Chef Registration</li><li>FAQS</li><li>Blog</li><li>Terms of service</li><li>Cookies</li></ul>
  </div>
</footer>
<div class="bottom-bar">Daniel Whitcombe © 2019 All Rights Reserved | Privacy Policy | Terms and Conditions</div>

</body>
</html>
```